Business Intelligence/Analytics Technology Company Business Card

We are a higher-end enterprise software development company working with Retailer POS data to provide business intelligence and analytical services to fortune 500 companies.

I have an immediate need for a professional/thick/bold business card. The same design aspects will spiral into more media such as flyers/folders/etc...

Our website is www.brenvolq.com for our product.

I like "Clean" designs if that makes sense, not a lot of "stuff".

The uploaded files, the A logo with the box is the style we're leaning towards, but the A logo without the blue box is all good too... get creative.

Target Market(s)

Executives of large companies, down to VP level..

Industry/Entity Type

Software

Requirements
Must have
• I'm wanting a thick designer like business card.

I think we're going to change our logo to a more quillmesh 8 looking style... http://www.brenvolq.com/card.ai as an example of our current business card.

The winner will also have knowledge of where i can get these things printed.
Nice to have
• Blue-ish color scheme? I'm open to anything. Our Competition is Red, and another is Green. So we'll stick with the Blue.

```html
<!DOCTYPE html>
<html lang="en">
<head>
<meta charset="utf-8">
<title>BRENVOLQ Business Card</title>
<link href="https://fonts.googleapis.com/css2?family=Source+Sans+3:wght@400;600&display=swap" rel="stylesheet">
<style>
  :root {
    --brand-blue: #0a6ccc;
    --brand-blue-deep: #065bb3;
    --paper: #ffffff;
    --backdrop: #3b3b3d;
    --ink-blue: #1266c4;
  }
  * { margin: 0; padding: 0; box-sizing: border-box; }
  html, body {
    width: 1200px; height: 900px; overflow: hidden;
    background: var(--backdrop);
    font-family: "Source Sans 3", sans-serif;
  }
  .stage { position: relative; width: 1200px; height: 900px; }
  .card {
    position: absolute; top: 308px;
    width: 513px; height: 285px;
    border-radius: 18px; overflow: hidden;
    background: var(--paper);
    box-shadow: 0 2px 6px rgba(0,0,0,.35);
  }
  .card--front { left: 73px; }
  .card--back { left: 615px; }
  .card__shape { position: absolute; inset: 0; width: 513px; height: 285px; }

  /* front */
  .front-mark {
    position: absolute; left: 232px; top: 52px;
    width: 48px; height: 48px; background: var(--paper);
  }
  .front-wordmark {
    position: absolute; left: 0; right: 0; top: 140px;
    text-align: center; color: var(--paper);
    font-size: 32px; font-weight: 400; letter-spacing: .42em;
    padding-left: .42em; line-height: 1;
  }
  .front-url {
    position: absolute; left: 0; right: 0; top: 250px;
    display: flex; justify-content: center; align-items: center; gap: 5px;
    color: var(--ink-blue); font-size: 15px;
  }

  /* back */
  .back-brand {
    position: absolute; left: 44px; top: 42px;
    display: flex; align-items: center; gap: 22px;
  }
  .back-mark { width: 58px; height: 62px; background: var(--brand-blue); }
  .back-wordmark {
    color: var(--brand-blue); font-size: 29px; font-weight: 400;
    letter-spacing: .42em; line-height: 1;
  }
  .person {
    position: absolute; left: 44px; top: 143px;
    color: var(--ink-blue); font-size: 19px; line-height: 1;
  }
  .person__role { font-size: 15px; }
  .contacts {
    position: absolute; left: 45px; top: 207px;
    list-style: none; color: var(--paper); font-size: 12.5px; line-height: 14.6px;
  }
  .contacts li { display: flex; align-items: center; gap: 6px; }
  .contacts svg { width: 10px; height: 10px; flex: none; }
  .address {
    position: absolute; left: 313px; top: 214px;
    color: var(--paper); font-size: 12.5px; line-height: 14.6px; font-style: normal;
  }
  .address__company { font-weight: 600; }
</style>
</head>
<body>
<main class="stage">

  <section class="card card--front" aria-label="Card front">
    <svg class="card__shape" viewBox="0 0 513 285" aria-hidden="true">
      <path d="M0 0 H513 V193 Q300 236 0 218 Z" fill="var(--brand-blue)"/>
      <path d="M70 226 Q330 232 513 205 V212 Q330 240 70 226 Z" fill="var(--brand-blue)"/>
    </svg>
    <div class="front-mark"></div>
    <div class="front-wordmark">BRENVOLQ</div>
    <div class="front-url">
      <svg width="11" height="11" viewBox="0 0 12 12" aria-hidden="true">
        <circle cx="6" cy="6" r="5.2" fill="none" stroke="var(--ink-blue)" stroke-width="1.3"/>
        <ellipse cx="6" cy="6" rx="2.2" ry="5.2" fill="none" stroke="var(--ink-blue)" stroke-width="1"/>
        <line x1="1" y1="6" x2="11" y2="6" stroke="var(--ink-blue)" stroke-width="1"/>
      </svg>
      <span>www.brenvolq.com</span>
    </div>
  </section>

  <section class="card card--back" aria-label="Card back">
    <svg class="card__shape" viewBox="0 0 513 285" aria-hidden="true">
      <path d="M0 182 Q260 192 513 149 V285 H0 Z" fill="var(--brand-blue)"/>
      <path d="M70 186 Q300 190 400 176 Q300 186 70 186 Z" fill="var(--paper)"/>
    </svg>
    <div class="back-brand">
      <div class="back-mark"></div>
      <div class="back-wordmark">BRENVOLQ</div>
    </div>
    <p class="person">Marcus Velden <span class="person__role">| President</span></p>
    <ul class="contacts">
      <li>
        <svg viewBox="0 0 10 10" aria-hidden="true"><rect x="2.5" y=".5" width="5" height="9" rx="1" fill="none" stroke="#fff" stroke-width="1"/><rect x="4.2" y="7.3" width="1.6" height="1" fill="#fff"/></svg>
        555 210 4417
      </li>
      <li>
        <svg viewBox="0 0 10 10" aria-hidden="true"><circle cx="5" cy="5" r="5" fill="#fff"/><path d="M3.2 2.5 L4.2 3.6 L3.7 4.3 Q4.6 5.8 5.9 6.4 L6.5 5.9 L7.6 6.8 L7 7.7 Q4.5 7.5 2.5 3.2 Z" fill="var(--brand-blue)"/></svg>
        555 384 9021
      </li>
      <li>
        <svg viewBox="0 0 10 10" aria-hidden="true"><rect x="2.5" y=".5" width="5" height="3" fill="#fff"/><rect x=".5" y="3.5" width="9" height="4" rx="1" fill="#fff"/><rect x="2.5" y="6.5" width="5" height="3" fill="#fff"/></svg>
        555 672 1350
      </li>
      <li>
        <svg viewBox="0 0 10 10" aria-hidden="true"><rect x=".5" y="2" width="9" height="6.5" fill="#fff"/><path d="M.5 2 L5 5.6 L9.5 2" fill="none" stroke="var(--brand-blue)" stroke-width="1"/></svg>
        marcus@brenvolq.com
      </li>
    </ul>
    <address class="address">
      <div class="address__company">BRENVOLQ Technology Group, Inc</div>
      <div>48 Larkspur Lane</div>
      <div>Fairmont, New York 10482</div>
    </address>
  </section>

</main>
</body>
</html>
```